Redesign Company Website

Cellar Bridge new website: www.cellarbridge.example.com.au

Brief

• Cellar Bridge
Cellar Bridge is a relationship marketing company offering telesales services to partner wineries. We manage the winery’s database, engage in telesales campaigns and return great sales results to the winery.
Cellar Bridge currently operates in Australia, New Zealand and Canada, with plans to expand to the USA in 2014.

• The service
We take the winery’s database, clean it up, and typically run 2 telesales campaigns per year. The timing, products and pricing are agreed with the winery prior to the campaign.
There are multiple benefits for the winery: the database is engaged with the winery, sales conversions are high and the database is reliable and up to date.

• The size of the company
Cellar Bridge International employs about 20 people and plans to grow to 30. The turnover is in excess of AU$5m

• How long have you been established?
Cellar Bridge was rebranded 12 months ago, but the original entity has been trading for 10 years.

• The company in a few words
Dynamic
Responsive
Detailed
Bright
Independent
Friendly
Engaging

The old web site

www.cellarbridge.example.com.au

• What is good about the web site?
Clean look, succinct. No need to scroll down to get information.

• What don’t you like about the old web site?
Blocky top graphics look too cartoon-like
Stock photos
Dull, corporate look with no personality
Bad infographic on Services page
Limited contact information
Too much red

The new web site

• Outline the aims of the new web site
The main aim of the new website is to represent Cellar Bridge and its personality better. We hope to be able to engage wineries to come back to the site. It has to contain the relevant service and benefit information to convert new winery business.

• Who is the target audience?
This is above all a B2B website aimed at winery partners
It is not an e-commerce site, but we want wineries to come back frequently.

• How will your target audience be accessing your site
All forms, probably including mobile phones.

• What are the unique selling points for your company, your products or your services?
Independent
Reliable
Secure

• Competitors' web sites:
www.harvestcrewsample.com.au
http://www.morrowvaleestatesdirect.com.au/

The look and feel of the new web site

• Various web sites that we like the look & feel of.
http://www.tessbrook.com.au/ Great graphic on home page, good use of white space, uncluttered
http://pelvaquin.com/ Good use of space, clear navigation, bit quirky
http://www.casaremoli.com.au/ Ease of navigation, like the drop down “where we are” on the home page
http://www.starlanternrecaps.co.uk/ Great use of graphics for navigation etc.

• Logo and sample of corporate identity files attached.

Target Market(s)

Wineries in Australia, NZ, Canada, USA

Industry/Entity Type

E-Commerce

Requirements
Nice to have
• Would be good to have a blog on the site to create new content easily and frequently

```html
<!DOCTYPE html>
<html lang="en">
<head>
<meta charset="utf-8">
<title>Cellar Bridge</title>
<link href="https://fonts.googleapis.com/css2?family=Oswald:wght@300;400&family=Open+Sans:wght@400;600&display=swap" rel="stylesheet">
<style>
:root{
  --red:#e0161e;
  --ink:#2b2b2b;
  --topbar:#262323;
  --page:#f1f1f1;
  --line:#d8d8d8;
  --footer:#474747;
  --footer-line:#5a5a5a;
  --quote:#3a3a3a;
  --muted:#cfcfcf;
}
*{box-sizing:border-box;margin:0;padding:0}
html,body{width:913px;height:1200px;overflow:hidden}
body{font-family:"Open Sans",Arial,sans-serif;color:var(--ink);background:var(--page)}
.canvas{position:relative;width:913px;height:1200px;overflow:hidden;background:var(--page)}
a{color:inherit;text-decoration:none}
.abs{position:absolute}

/* top bar */
.topbar{left:0;top:0;width:913px;height:36px;background:var(--topbar);border-bottom:2px solid var(--red)}
.topbar .lead{left:105px;top:10px;font-size:11px;color:#e8e8e8}
.regions{right:106px;top:0;display:flex;height:34px}
.regions li{list-style:none;font-family:Arial,sans-serif;font-size:9.5px;color:#ddd;padding:0 10px;line-height:34px;border-left:1px solid #444;position:relative}
.regions li:last-child{border-right:1px solid #444}
.regions li.active{color:#fff}
.regions li.active:after{content:"";position:absolute;left:50%;bottom:0;margin-left:-4px;border:4px solid transparent;border-bottom-color:var(--red)}

/* header */
.brand{left:105px;top:47px;width:140px;height:51px;background:#fff;display:flex;align-items:center;gap:6px;padding-left:6px}
.brand .mark{width:10px;height:10px;background:var(--red)}
.brand .name{font-size:17px;font-weight:600;color:var(--red)}
.callout{right:106px;top:52px;text-align:right;font-size:14px;line-height:21px;color:#333}
.callout a{color:var(--red)}

/* nav */
.nav{left:105px;top:108px;width:702px;height:34px;background:#f7f7f7;border:1px solid var(--line);display:flex}
.nav .home{width:41px;height:34px;margin:-1px 0 0 -1px;background:var(--red);display:flex;align-items:center;justify-content:center;position:relative}
.nav .home:after{content:"";position:absolute;bottom:-5px;left:50%;margin-left:-5px;border:5px solid transparent;border-bottom:0;border-top-color:var(--red)}
.nav li{list-style:none;font-family:Arial,sans-serif;font-size:9.5px;color:#333;padding:0 17px;line-height:32px;border-right:1px solid var(--line)}

/* slider */
.slider{left:105px;top:157px;width:702px;height:244px;border-radius:2px;background:linear-gradient(180deg,#2c1d12 0%,#6b4a2a 45%,#8a6a45 62%,#2b241d 85%,#4a3f35 100%)}
.dots{left:117px;top:378px;display:flex;gap:8px}
.dots span{width:13px;height:13px;border-radius:50%;background:#fff}
.dots span.on{background:var(--red)}

/* section headings */
.head-row{display:flex;align-items:center;gap:9px}
.h-cond{font-family:"Oswald",sans-serif;font-weight:300;text-transform:uppercase;color:#222;letter-spacing:-.2px;white-space:nowrap}
.rule{flex:1;height:7px;background:repeating-linear-gradient(90deg,#ddd 0 1px,transparent 1px 3px),repeating-linear-gradient(0deg,#ddd 0 1px,transparent 1px 3px)}

/* services sidebar */
.services-head{left:105px;top:420px;width:154px}
.services-head .h-cond{font-size:15px}
.svc-open{left:105px;top:445px;font-size:10px;color:var(--red);display:flex;align-items:center;gap:7px}
.box-ic{width:10px;height:10px;display:flex;align-items:center;justify-content:center}
.svc-open .box-ic{background:var(--red)}
.box-ic i{display:block;width:6px;height:1.5px;background:#fff;position:relative}
.svc-list .box-ic{background:#222}
.box-ic.plus i:after{content:"";position:absolute;left:2.25px;top:-2.25px;width:1.5px;height:6px;background:#fff}
.sub{left:110px;top:472px;width:150px;border-left:6px solid #e2e2e2;padding-left:11px}
.sub li{list-style:none;font-size:9px;color:var(--red);height:21px;line-height:21px}
.svc-list{left:105px;top:588px}
.svc-list li{list-style:none;display:flex;align-items:center;gap:7px;font-size:10px;height:24px;color:#222}

/* welcome */
.welcome{left:273px;top:424px;width:534px;height:159px;background:#fafafa;border:1px solid #ddd;box-shadow:inset 0 0 0 3px #f1f1f1;padding:13px 15px}
.welcome h2{font-size:14px;margin-bottom:6px}
.welcome p{font-size:8.9px;line-height:12.6px;color:#444;margin-bottom:12px}
.welcome .more{font-size:9px;color:var(--red)}

/* international */
.intl-head{left:273px;top:600px;width:534px}
.intl-head .h-cond{font-size:14px}
.arrows{display:flex;gap:2px}
.arrows span{width:17px;height:14px;display:flex;align-items:center;justify-content:center;background:#333}
.arrows span.next{background:var(--red)}
.intl-head .arrows{margin-left:4px}
.intl-copy{left:273px;top:627px;width:534px;font-size:8.9px;line-height:12.8px;color:#444}
.card{top:666px;width:169px}
.card .frame{width:169px;height:147px;background:#fff;border:1px solid #d6d6d6;padding:4px}
.card .photo{width:100%;height:100%}
.card .cap{margin-top:9px;text-align:center;font-size:9px;line-height:14px;color:#222}
.card .details{display:block;text-align:center;font-size:12px;color:var(--red);text-decoration:underline;margin-top:3px;padding-bottom:5px;border-bottom:1px solid #bbb}
.zoom{position:absolute;left:72px;top:58px;width:29px;height:27px;background:var(--red);display:flex;align-items:center;justify-content:center}

/* footer */
.footer{left:0;top:913px;width:913px;height:161px;background:var(--footer);border-top:2px solid var(--red)}
.fcol{top:26px;color:#ddd}
.fcol h3{font-family:"Oswald",sans-serif;font-weight:300;font-size:14px;color:#fff;text-transform:uppercase;margin-bottom:9px}
.fcol p,.fcol li{font-size:8.5px;line-height:12.8px;color:#ddd}
.fcol li{list-style:none;line-height:19px}
.nowrap{white-space:nowrap}
.sep{top:24px;width:1px;height:113px;background:var(--footer-line)}
.field{width:191px;height:22px;background:#fff;border:1px solid #ccc;font-size:8.5px;font-style:italic;color:#999;padding:5px 6px;margin-bottom:10px}
.submit{width:71px;height:22px;margin-left:120px;background:linear-gradient(#37b421,#237d16);color:#fff;font-size:10.5px;font-weight:600;display:flex;align-items:center;justify-content:center;border-radius:2px}

.quotebar{left:0;top:1073px;width:913px;height:54px;background:var(--quote)}
.avatar{left:105px;top:10px;width:36px;height:36px;background:linear-gradient(#d8d8d8,#9a9a9a);border:2px solid #ddd}
.quote{left:153px;top:13px;width:560px;font-size:9.2px;line-height:14px;color:#eee}
.q-arrows{left:755px;top:19px}
.q-arrows span{width:23px;height:16px}

.bottom{left:0;top:1127px;width:913px;height:73px;background:#333}
.copy{left:105px;top:30px;font-size:9px;color:#ccc}
.copy b{color:#fff;font-weight:400}
.social{right:106px;top:26px;display:flex;gap:4px}
.social span{width:19px;height:19px;background:#4a4a4a;border:1px solid #5c5c5c}
</style>
</head>
<body>
<div class="canvas">

  <header class="abs topbar">
    <div class="abs lead">Contact Your Local Cellar Bridge Representative Today</div>
    <ul class="abs regions">
      <li class="active">AUSTRALIA</li><li>NEW ZEALAND</li><li>HONG KONG</li><li>CANADA</li>
    </ul>
  </header>

  <div class="abs brand"><span class="mark"></span><span class="name">Cellar Bridge</span></div>
  <div class="abs callout">
    Call Us Now : <a href="#">1800-555-014</a><br>
    E-mail : <a href="#">info@cellarbridge.example.com.au</a>
  </div>

  <nav>
    <ul class="abs nav">
      <li class="home" style="padding:0;border:0">
        <svg width="14" height="13" viewBox="0 0 14 13"><path d="M7 1 L1 6.5 H3 V12 H6 V8.5 H8 V12 H11 V6.5 H13 Z" fill="#fff"/></svg>
      </li>
      <li>ABOUT US</li><li>SERVICES</li><li>BENEFITS</li><li>TESTIMONIALS</li><li>BLOG</li><li>CONTACT US</li>
    </ul>
  </nav>

  <div class="abs slider" role="img" aria-label="Row of wine bottles and empty wine glasses on a bar counter in warm light"></div>
  <div class="abs dots"><span class="on"></span><span></span><span></span><span></span></div>

  <aside>
    <div class="abs head-row services-head"><span class="h-cond">Services</span><span class="rule"></span></div>
    <div class="abs svc-open"><span class="box-ic"><i></i></span>LOREM IPSUM DOLOR SIT</div>
    <ul class="abs sub">
      <li>Lorem ipsum dolor sit amet</li><li>Lorem ipsum dolor sit amet</li><li>Lorem ipsum dolor sit amet</li><li>Lorem ipsum dolor sit amet</li><li>Lorem ipsum dolor sit amet</li>
    </ul>
    <ul class="abs svc-list">
      <li><span class="box-ic plus"><i></i></span>LOREM IPSUM DOLOR SIT</li>
      <li><span class="box-ic plus"><i></i></span>LOREM IPSUM DOLOR SIT</li>
      <li><span class="box-ic plus"><i></i></span>LOREM IPSUM DOLOR SIT</li>
      <li><span class="box-ic plus"><i></i></span>LOREM IPSUM DOLOR SIT</li>
      <li><span class="box-ic plus"><i></i></span>LOREM IPSUM DOLOR SIT</li>
      <li><span class="box-ic plus"><i></i></span>LOREM IPSUM DOLOR SIT</li>
      <li><span class="box-ic plus"><i></i></span>LOREM IPSUM DOLOR SIT</li>
      <li><span class="box-ic plus"><i></i></span>LOREM IPSUM DOLOR SIT</li>
      <li><span class="box-ic plus"><i></i></span>LOREM IPSUM DOLOR SIT</li>
      <li><span class="box-ic plus"><i></i></span>LOREM IPSUM DOLOR SIT</li>
      <li><span class="box-ic plus"><i></i></span>LOREM IPSUM DOLOR SIT</li>
      <li><span class="box-ic plus"><i></i></span>LOREM IPSUM DOLOR SIT</li>
    </ul>
  </aside>

  <section class="abs welcome">
    <h2 class="h-cond">Welcome to Cellar Bridge</h2>
    <p>Cellar Bridge was founded in 2004 and rebranded in 2012 to by committed and enthusiastic wine professionals. The management team has almost half a century of combined winery direct management experience to offer something that isn't provided by the major supermarkets: great service, fantastic wine and long term relationships.</p>
    <p>We have long-established connections in the marketplace and our sales team is passionate, dedicated and highly trained. We want to learn everything there is to know about our clients' products and the people who enjoy them.</p>
    <a class="more" href="#">Read More &raquo;</a>
  </section>

  <section>
    <div class="abs head-row intl-head">
      <span class="h-cond">Cellar Bridge International</span>
      <span class="rule"></span>
      <span class="arrows">
        <span><svg width="6" height="8"><path d="M5 0.5 L1.5 4 L5 7.5" stroke="#fff" stroke-width="1.6" fill="none"/></svg></span>
        <span class="next"><svg width="6" height="8"><path d="M1 0.5 L4.5 4 L1 7.5" stroke="#fff" stroke-width="1.6" fill="none"/></svg></span>
      </span>
    </div>
    <p class="abs intl-copy">Cellar Bridge is the first agency offering international service. We have offices in Australia, New Zealand and Canada. Ask us how we can help you in these countries and more.</p>

    <article class="abs card" style="left:273px">
      <div class="frame" style="position:relative">
        <div class="photo" role="img" aria-label="Pale wine bottles and a glass of red wine, softly faded" style="background:linear-gradient(135deg,#e9dcc4,#d8c6a6 50%,#c9b08f)"></div>
        <span class="zoom"><svg width="13" height="13" viewBox="0 0 13 13"><rect x="1" y="1" width="11" height="11" fill="none" stroke="#fff" stroke-width="1.3"/><path d="M4 4 L9 9 M9 5.5 V9 H5.5" stroke="#fff" stroke-width="1.3" fill="none"/></svg></span>
      </div>
      <div class="cap">LOREM IPSUM DOLOR SIT AMET<br>CONSECTETUR ADIPISCING</div>
      <a class="details" href="#">More Details</a>
    </article>

    <article class="abs card" style="left:456px">
      <div class="frame"><div class="photo" role="img" aria-label="Four wine bottles of white, rosé and red wine in a row" style="background:linear-gradient(90deg,#cfc79a,#c9665a 40%,#3a3230 70%,#7a2a2a)"></div></div>
      <div class="cap">LOREM IPSUM DOLOR SIT AMET<br>CONSECTETUR ADIPISCING</div>
      <a class="details" href="#">More Details</a>
    </article>

    <article class="abs card" style="left:638px">
      <div class="frame"><div class="photo" role="img" aria-label="Glass of red wine beside a dark bottle and red grapes on a red backdrop" style="background:linear-gradient(160deg,#b3121a,#7d0d12 55%,#3b1014)"></div></div>
      <div class="cap">LOREM IPSUM DOLOR SIT AMET<br>CONSECTETUR ADIPISCING</div>
      <a class="details" href="#">More Details</a>
    </article>
  </section>

  <footer class="abs footer">
    <div class="abs fcol" style="left:105px">
      <h3>Information</h3>
      <ul>
        <li>&rarr; About Us</li><li>&rarr; Services</li><li>&rarr; Benefits</li><li>&rarr; Testimonials</li><li>&rarr; Contact Us</li>
      </ul>
    </div>
    <div class="abs sep" style="left:224px"></div>
    <div class="abs fcol" style="left:253px;width:150px">
      <h3>Blog</h3>
      <p>Prices will be as specified on the website and are exclusive of Delivery Charges and VAT.</p>
      <p style="margin-top:12px">The Total Price (to include Delivery Charges and VAT) will be stated on the Acknowledgement of Order.</p>
    </div>
    <div class="abs sep" style="left:413px"></div>
    <div class="abs fcol" style="left:441px;width:160px">
      <h3>Contact Details</h3>
      <p>Or drop in if you're in town:<br>118 Cask Row,<br>Millbrook NSW 2099</p>
      <p class="nowrap" style="margin-top:12px">Tel: 1800 555 014<br>Email: info@cellarbridge.example.com.au</p>
    </div>
    <div class="abs sep" style="left:603px"></div>
    <div class="abs fcol" style="left:616px">
      <h3>Newsletter Signup</h3>
      <div class="field">Enter your name</div>
      <div class="field">Enter your email</div>
      <div class="submit">SUBMIT</div>
    </div>
  </footer>

  <div class="abs quotebar">
    <div class="abs avatar" role="img" aria-label="Customer portrait placeholder"></div>
    <p class="abs quote">Lorem ipsum dolor sit amet, consectetur adipiscing elit. Fusce at nisi in felis molestie porta sed at lectus. Duis euismod vestibulum interdum. Aenean semper molestie aliquet. Maecenas ornare urna sed massa adipiscing.</p>
    <div class="abs arrows q-arrows">
      <span><svg width="7" height="10"><path d="M6 1 L2 5 L6 9" stroke="#fff" stroke-width="2" fill="none"/></svg></span>
      <span class="next"><svg width="7" height="10"><path d="M1 1 L5 5 L1 9" stroke="#fff" stroke-width="2" fill="none"/></svg></span>
    </div>
  </div>

  <div class="abs bottom">
    <div class="abs copy">Copyright &copy; 2013 <b>cellarbridge.example.com.au</b>. All rights reserved</div>
    <div class="abs social"><span></span><span></span><span></span><span></span><span></span><span></span></div>
  </div>

</div>
</body>
</html>
```